snugSEAL - packaging design for plastic zip-lock mechansim

Looking for packaging designs for my patented product, which provides the ability to lock and close existing plastic bags, which have been opened up (like sugar or flour bag, snack bag, etc.). With applying snugSEAL to any bag once opened, the products can be held safe, locked and dry.
Please check my supporting documentation attached, including logos and packaging description.
The packaging design has to make clear to the customer:
- WHAT is this product for
- how to USA
- what are the BENEFITS and the VALUE
I am looking for a long term cooperation with the winning designer, as I will need multiple variations of the packaging depending on individual product usage. I am thinking of approximately 10 different variations in the future.
Updates
Project Deadline Extended Reason: Extending deadline to receive more designs. Please submit your designs according to my description. Let me know if any questions!This will be a long term cooperation as I will need subsequent designs for alternative product variations in the future. Added Saturday, October 22, 2016
Target Market(s)
All consumers who buy products in the supermarket. In particular when they buy products in bags (like salt, sugar, flour, detergents, snacks, ...)
Industry/Entity Type
Retail
Look and feel
Each slider illustrates characteristics of the customer's brand and the style your logo design should communicate.

```html
<!DOCTYPE html>
<html lang="en">
<head>
<meta charset="utf-8">
<title>snugSEAL – Packaging</title>
<link rel="stylesheet" href="https://fonts.googleapis.com/css2?family=Noto+Sans:wght@400;700&family=Oswald:wght@500;700&display=swap">
<style>
  :root{
    --navy:#154a7e;
    --blue:#2f78b6;
    --mid:#3a8ac4;
    --sky:#a9e4fb;
    --ice:#d6ecfb;
    --arrow:#7fb4dc;
    --paper:#ffffff;
    --ink:#1b2a3a;
    --stage-top:#ffffff;
    --stage-bottom:#c9c9c9;
  }
  *{margin:0;padding:0;box-sizing:border-box}
  html,body{width:1200px;height:900px;overflow:hidden}
  body{position:relative;background:linear-gradient(180deg,var(--stage-top) 40%,var(--stage-bottom) 100%);font-family:"Noto Sans",sans-serif}

  .feature-board{position:absolute;left:0;top:0;width:612px;height:900px;overflow:hidden}
  .feature-board > .board-art{position:absolute;left:0;top:0}
  .feature-list{position:absolute;left:14px;top:36px;list-style:none}
  .feature-list li{display:flex;align-items:center;height:88px;color:var(--sky);font-weight:700;font-size:43px;letter-spacing:.2px;white-space:nowrap}
  .feature-list .bullet{display:block;width:22px;height:22px;margin-right:22px;flex:none}

  .pack{position:absolute;left:775px;top:42px;width:193px;height:855px;overflow:hidden}
  .pack > .pack-art{position:absolute;left:0;top:0}
  .pack-brand{position:absolute;left:0;top:34px;width:100%;text-align:center;font-size:27px;font-weight:400;color:var(--ink);letter-spacing:.5px;line-height:36px}
  .pack-title{position:absolute;left:0;top:288px;width:100%;text-align:center;font-family:"Oswald",sans-serif;color:var(--sky);line-height:1}
  .pack-title .big{display:block;font-size:60px;font-weight:700;letter-spacing:5px}
  .pack-title .small{display:block;font-size:17px;font-weight:700;letter-spacing:1px;margin:6px 0 10px}
  .pack-title .size{display:block;font-size:21px;font-weight:700;letter-spacing:1.5px;margin-top:14px}
  .pack-features{position:absolute;left:18px;top:505px;list-style:none}
  .pack-features li{display:flex;align-items:center;height:25px;color:var(--sky);font-weight:700;font-size:12.5px;white-space:nowrap}
  .pack-features .bullet{display:block;width:9px;height:9px;margin-right:7px;flex:none}
  .pack-count{position:absolute;right:8px;top:790px;font-weight:700;font-size:15px;color:var(--navy)}
  .pack-footer{position:absolute;left:7px;top:823px;width:178px;font-size:6.5px;line-height:1.25;color:var(--ink)}
  .pack-web{position:absolute;right:10px;top:842px;font-size:7px;font-weight:700;color:var(--ink);letter-spacing:.4px}
</style>
</head>
<body>

<section class="feature-board">
  <svg class="board-art" width="612" height="900" viewBox="0 0 612 900">
    <defs>
      <linearGradient id="boardTop" x1="0" y1="0" x2="1" y2="0">
        <stop offset="0" stop-color="#3a86c0"/>
        <stop offset="1" stop-color="#154a7e"/>
      </linearGradient>
      <linearGradient id="productArea" x1="0" y1="0" x2="1" y2="0">
        <stop offset="0" stop-color="#b9d8fa"/>
        <stop offset=".5" stop-color="#e6f1fd"/>
        <stop offset="1" stop-color="#9cc3f2"/>
      </linearGradient>
      <radialGradient id="circleFill" cx=".5" cy=".5" r=".5">
        <stop offset="0" stop-color="#ffffff"/>
        <stop offset="1" stop-color="#cfe0fb"/>
      </radialGradient>
    </defs>
    <rect class="product-photo" role="img" aria-label="Close-up of blue seal strips" x="0" y="380" width="612" height="520" fill="url(#productArea)"/>
    <path class="wave-band" d="M0 390 C120 392 260 420 380 470 C470 505 560 560 612 600 V520 C540 470 440 430 300 410 C180 395 80 385 0 385 Z" fill="var(--mid)"/>
    <path class="board-header" d="M0 0 H612 V520 C540 470 440 430 300 410 C180 395 80 385 0 385 Z" fill="url(#boardTop)"/>
    <circle cx="430" cy="478" r="133" fill="var(--mid)"/>
    <circle class="howto-art" role="img" aria-label="Cut-to-length instruction illustration" cx="430" cy="478" r="121" fill="url(#circleFill)"/>
  </svg>
  <ul class="feature-list">
    <li><svg class="bullet" viewBox="0 0 22 22"><path d="M2 8h10V3l8 8-8 8v-5H2z" fill="var(--arrow)"/></svg>Adjustable in length</li>
    <li><svg class="bullet" viewBox="0 0 22 22"><path d="M2 8h10V3l8 8-8 8v-5H2z" fill="var(--arrow)"/></svg>Easy to attach</li>
    <li><svg class="bullet" viewBox="0 0 22 22"><path d="M2 8h10V3l8 8-8 8v-5H2z" fill="var(--arrow)"/></svg>Fully to recycle</li>
  </ul>
</section>

<section class="pack">
  <svg class="pack-art" width="193" height="855" viewBox="0 0 193 855">
    <defs>
      <linearGradient id="packPanel" x1="0" y1="0" x2="1" y2="1">
        <stop offset="0" stop-color="#2f78b6"/>
        <stop offset="1" stop-color="#123f6e"/>
      </linearGradient>
      <linearGradient id="packWindow" x1="0" y1="0" x2="1" y2="0">
        <stop offset="0" stop-color="#9cc6f4"/>
        <stop offset=".5" stop-color="#d9eafc"/>
        <stop offset="1" stop-color="#8fbcef"/>
      </linearGradient>
    </defs>
    <rect width="193" height="855" fill="var(--paper)"/>
    <rect x="78" y="11" width="36" height="7" rx="3.5" fill="#111"/>
    <rect class="product-photo" role="img" aria-label="Rolled seal strips seen through the pack" x="0" y="100" width="193" height="210" fill="url(#packWindow)"/>
    <path d="M0 86 C60 84 130 88 193 100 V108 C130 96 60 92 0 94 Z" fill="var(--blue)"/>
    <rect class="product-photo" role="img" aria-label="Seal strips seen through the pack" x="0" y="600" width="193" height="200" fill="url(#packWindow)"/>
    <path d="M0 258 C60 248 130 250 193 262 V640 C130 665 60 655 0 650 Z" fill="url(#packPanel)"/>
    <path d="M0 650 C60 655 130 665 193 640 V652 C130 676 60 666 0 662 Z" fill="var(--mid)"/>
    <circle cx="142" cy="630" r="40" fill="var(--mid)"/>
    <circle class="howto-art" role="img" aria-label="Cut-to-length instruction illustration" cx="142" cy="630" r="36" fill="#f2f7fe"/>
    <rect x="0" y="800" width="193" height="55" fill="var(--paper)"/>
  </svg>
  <div class="pack-brand">snugSEAL</div>
  <div class="pack-title">
    <span class="big">LOCK</span>
    <span class="small">PAPER &amp; PLASTIC</span>
    <span class="big">BAGS</span>
    <span class="size">UP TO 25 CM</span>
  </div>
  <ul class="pack-features">
    <li><svg class="bullet" viewBox="0 0 22 22"><path d="M2 8h10V3l8 8-8 8v-5H2z" fill="var(--arrow)"/></svg>Adjustable in length</li>
    <li><svg class="bullet" viewBox="0 0 22 22"><path d="M2 8h10V3l8 8-8 8v-5H2z" fill="var(--arrow)"/></svg>Easy to attach</li>
    <li><svg class="bullet" viewBox="0 0 22 22"><path d="M2 8h10V3l8 8-8 8v-5H2z" fill="var(--arrow)"/></svg>Fully to recycle</li>
  </ul>
  <div class="pack-count">x10</div>
  <p class="pack-footer">Lorem ipsum dolor, sit amet, consectuer. Lorem ipsum dolor, sit amet, consectuer.</p>
  <div class="pack-web">WWW.SNUGSEAL.COM</div>
</section>

</body>
</html>
```